Makeup Artist Requires Business Card design

Hi

I am looking for a business card design to market my makeup artist business. I operate under my own name Mara Veldt and I would like to keep the design of the card very simplistic and chic - something that keeps both my name and profession (makeup artist) the focus of the card. I would like it to be a style that is eyecatching to the reader (i am open to anything unusual) but upmarket.

Target Market(s)

women, magazine/beauty/fashion editors, photographers.

Industry/Entity Type

Business

Requirements
Must have
• Must contain:

Phone number: 0418 372 915
Website: www.maraveldt.com.au
email: contact@maraveldt.com.au

(although you don't need to have prefaced these with the words phone number, website etc :))
Should not have
• I am not looking for anything overly colorful - my preference is to keep the card dark if possible.

```html
<!DOCTYPE html>
<html lang="en">
<head>
<meta charset="utf-8">
<title>Mara Veldt – Make-Up Artist Business Card</title>
<link rel="stylesheet" href="https://fonts.googleapis.com/css2?family=Great+Vibes&family=Advent+Pro:wght@300;400&display=swap">
<style>
  :root {
    --backdrop: #e9e7e4;
    --card-centre: #3b3b3b;
    --card-edge: #1f1f1f;
    --script-ink: #1b1b1b;
    --emboss-light: rgba(255, 255, 255, 0.14);
    --profession-ink: #4a4a4a;
    --contact-ink: #f4f4f4;
    --accent-blue: #1e90e8;
  }
  html, body {
    margin: 0;
    width: 1200px;
    height: 900px;
    overflow: hidden;
    background: var(--backdrop);
  }
  .business-card {
    position: absolute;
    left: 60px;
    top: 102px;
    width: 1080px;
    height: 696px;
    background: radial-gradient(ellipse 55% 60% at 50% 48%, var(--card-centre) 0%, #2a2a2a 55%, var(--card-edge) 100%);
    border-radius: 4px;
    box-shadow: 0 6px 18px rgba(0, 0, 0, 0.35);
    overflow: hidden;
  }
  .lips-motif {
    position: absolute;
    left: 24px;
    top: 40px;
    width: 62px;
    height: 42px;
  }
  .artist-name {
    position: absolute;
    left: 0;
    right: 0;
    top: 200px;
    margin: 0;
    text-align: center;
    font-family: "Great Vibes", cursive;
    font-weight: 400;
    font-size: 170px;
    line-height: 1;
    color: var(--script-ink);
    text-shadow: 0 2px 1px var(--emboss-light), 0 -1px 1px rgba(0, 0, 0, 0.6);
  }
  .profession {
    position: absolute;
    left: 0;
    right: 0;
    top: 488px;
    margin: 0;
    text-align: center;
    font-family: "Advent Pro", sans-serif;
    font-weight: 400;
    font-size: 46px;
    letter-spacing: 5px;
    color: var(--profession-ink);
  }
  .contact-row {
    position: absolute;
    left: 0;
    right: 0;
    top: 646px;
    height: 40px;
  }
  .contact-item {
    position: absolute;
    top: 0;
    height: 40px;
    display: flex;
    align-items: center;
    gap: 12px;
    white-space: nowrap;
    font-family: "Advent Pro", sans-serif;
    font-weight: 400;
    font-size: 21px;
    text-transform: uppercase;
    color: var(--contact-ink);
    text-shadow: 0 2px 3px rgba(0, 0, 0, 0.8);
  }
  .contact-item svg { flex: none; filter: drop-shadow(0 2px 2px rgba(0,0,0,0.7)); }
  .contact-phone { left: 52px; }
  .contact-web { left: 402px; }
  .contact-email { right: 52px; }
</style>
</head>
<body>
  <main class="business-card">
    <svg class="lips-motif" viewBox="0 0 62 42" role="img" aria-label="Small blue lips motif">
      <ellipse cx="31" cy="21" rx="31" ry="17" fill="var(--accent-blue)"/>
    </svg>

    <h1 class="artist-name">Mara Veldt</h1>
    <p class="profession">Make-Up Artist</p>

    <footer class="contact-row">
      <div class="contact-item contact-phone">
        <svg width="22" height="30" viewBox="0 0 22 30" aria-hidden="true">
          <path d="M5 2 L9 2 L10 9 L7 11 Q8 18 13 22 L16 20 L21 24 L19 28 Q10 29 5 20 Q1 12 5 2 Z" fill="var(--contact-ink)"/>
        </svg>
        <span>0418 372 915</span>
      </div>
      <div class="contact-item contact-web">
        <svg width="28" height="28" viewBox="0 0 28 28" aria-hidden="true">
          <rect x="1" y="3" width="26" height="17" rx="1.5" fill="none" stroke="var(--contact-ink)" stroke-width="2.4"/>
          <rect x="4" y="6" width="20" height="11" fill="var(--contact-ink)"/>
          <rect x="12" y="20" width="4" height="4" fill="var(--contact-ink)"/>
          <rect x="7" y="24" width="14" height="2.4" fill="var(--contact-ink)"/>
        </svg>
        <span>www.maraveldt.com.au</span>
      </div>
      <div class="contact-item contact-email">
        <svg width="30" height="22" viewBox="0 0 30 22" aria-hidden="true">
          <rect x="1" y="1" width="28" height="20" fill="var(--contact-ink)"/>
          <path d="M1 1 L15 13 L29 1 M1 21 L11 10 M29 21 L19 10" fill="none" stroke="#2a2a2a" stroke-width="1.5"/>
        </svg>
        <span>contact@maraveldt.com.au</span>
      </div>
    </footer>
  </main>
</body>
</html>
```